Design a "healthy, happy dog and cat" cheque/check background

I am looking for a few design concepts featuring a happy healthy dog and cat, that will be used as the background of a paper cheque/check.

This will require Photoshop and stock photos.

Here is the design brief: https://files.brivontel.net/sheet/48kQmZ2xTrWvLpN7aHcYeJ5uBdFsKo9GiRtXnVw3Lz/view?share=on

Colors

Designer to choose colors to be used in the design.

Requirements
Must have
• A happy dog and cat the main focus within the "empty" central part of the cheque/check, and a complementary background for the rest of the cheque, following the design guidelines in the attached google doc.

```html
<!DOCTYPE html>
<html lang="en">
<head>
<meta charset="utf-8">
<title>Dog and Cat Personal Cheque</title>
<link rel="stylesheet" href="https://fonts.googleapis.com/css2?family=Arimo:wght@400;700&family=Share+Tech+Mono&display=swap">
<style>
  :root {
    --backdrop: #000000;
    --paper: #ffffff;
    --cheque-green: #cfe8d8;
    --ink: #1a1a1a;
    --ink-soft: #333333;
    --rule: #3a3a3a;
    --field: #ffffff;
    --pet-warm: #d9a766;
    --pet-cool: #c9c2bb;
  }
  html, body {
    margin: 0;
    padding: 0;
    width: 1200px;
    height: 1000px;
    overflow: hidden;
    background: var(--backdrop);
  }
  .canvas { display: block; width: 1200px; height: 1000px; }
  .cheque-paper { fill: var(--paper); }
  .cheque-face { fill: var(--cheque-green); }
  .field-box { fill: var(--field); }
  .rule { stroke: var(--rule); stroke-width: 1.3; fill: none; }
  .text { font-family: "Arimo", Arial, sans-serif; fill: var(--ink-soft); }
  .holder-name { font-size: 20px; font-weight: 700; }
  .holder-address { font-size: 18px; }
  .cheque-number { font-size: 23px; font-weight: 700; fill: var(--ink); }
  .date-label { font-size: 19px; }
  .date-key { font-size: 13px; letter-spacing: 0; }
  .small-label { font-size: 13px; }
  .dollar-sign { font-size: 28px; }
  .amount-words { font-size: 14px; }
  .bank-name { font-size: 18px; font-weight: 700; fill: var(--ink); }
  .bank-address { font-size: 17px; letter-spacing: 0.4px; fill: var(--ink); }
  .company-name { font-size: 14px; fill: var(--ink); }
  .memo-label { font-size: 11px; }
  .micr-line { font-family: "Share Tech Mono", "Courier New", monospace; font-size: 27px; fill: var(--ink); letter-spacing: 2px; }
  .security-badge { fill: none; stroke: var(--ink-soft); stroke-width: 1; }
</style>
</head>
<body>
<svg class="canvas" viewBox="0 0 1200 1000" xmlns="http://www.w3.org/2000/svg">
  <defs>
    <linearGradient id="pet-tones" x1="0" y1="0" x2="1" y2="0">
      <stop offset="0" stop-color="var(--pet-warm)"/>
      <stop offset="0.55" stop-color="#e0c39a"/>
      <stop offset="1" stop-color="var(--pet-cool)"/>
    </linearGradient>
  </defs>

  <rect class="cheque-paper" x="26" y="236" width="1147" height="519"/>
  <rect class="cheque-face" x="50" y="255" width="1123" height="377"/>

  <rect class="pet-photo" x="330" y="275" width="450" height="357" rx="60" fill="url(#pet-tones)" opacity="0.85"
        role="img" aria-label="Photo of a golden puppy nuzzling a grey tabby kitten"/>

  <text class="text holder-name" x="82" y="314">Northpaw Cheque Co. Personal Cheque</text>
  <text class="text holder-address" x="82" y="334">15 Maple Row Lane</text>
  <text class="text holder-address" x="82" y="354">Lakeview, Ontario L2K 3P4</text>

  <text class="text cheque-number" x="1003" y="302">101</text>

  <text class="text date-label" x="776" y="358">DATE</text>
  <g class="date-fields">
    <rect class="field-box" x="838" y="322" width="34" height="35"/>
    <rect class="field-box" x="876" y="322" width="34" height="35"/>
    <rect class="field-box" x="914" y="322" width="34" height="35"/>
    <rect class="field-box" x="952" y="322" width="34" height="35"/>
    <rect class="field-box" x="990" y="322" width="34" height="35"/>
    <rect class="field-box" x="1028" y="322" width="34" height="35"/>
    <rect class="field-box" x="1066" y="322" width="34" height="35"/>
    <rect class="field-box" x="1104" y="322" width="34" height="35"/>
  </g>
  <g class="text date-key" text-anchor="middle">
    <text x="859" y="373">D</text><text x="897" y="373">D</text>
    <text x="935" y="373">M</text><text x="973" y="373">M</text>
    <text x="1011" y="373">Y</text><text x="1049" y="373">Y</text>
    <text x="1087" y="373">Y</text><text x="1117" y="373">Y</text>
  </g>

  <text class="text small-label" x="80" y="430">PAY TO THE</text>
  <text class="text small-label" x="80" y="443">ORDER OF</text>
  <path class="rule" d="M80 448 H908 V420"/>
  <text class="text dollar-sign" x="932" y="441">$</text>
  <rect class="field-box" x="957" y="403" width="184" height="46"/>

  <path class="rule" d="M80 499 H893 L898 468"/>
  <text class="text amount-words" x="905" y="491">100 DOLLARS</text>

  <circle cx="123" cy="548" r="26" fill="var(--ink)"/>
  <text class="text bank-name" x="173" y="538">Your Financial Institution</text>
  <text class="text bank-address" x="173" y="556">200 Finance Avenue</text>
  <text class="text bank-address" x="173" y="574">Your City, Your Province A1B 2CS</text>

  <text class="text company-name" x="800" y="567">Optional Company Name</text>

  <rect class="security-badge" x="1137" y="496" width="28" height="128"/>

  <text class="text memo-label" x="85" y="613">MEMO</text>
  <line class="rule" x1="85" y1="617" x2="1077" y2="617"/>

  <text class="micr-line" x="78" y="694">⑈101⑈ ⑆12345⑉678⑆ 12345⑉6789⑈</text>
</svg>
</body>
</html>
```